Create 33.5x79in Graphic for Rollup Marketing Banner

Hi,

I sell common home and kitchen products on Bazarly.com and other marketplaces. In a couple of weeks, I'm going to a trade show / flea market / bizarre and will be selling products onsite to customers. I want to create a roll-up marketing banner that introduces my company and products to people that walk by the booth.

I need the graphic design for 1 rollup banner that is 33.5 inches wide x 79 inches high in size. (85.1 x 200.6 CM).

Primary colors of banner should match the Flexwell Goods logo (attached).

Information for the banner:
1. Company: Flexwell Goods
2. Tag: Quality Products to Make Everyday Life Easier
3. various photos of products - some are attached (6 to 9+ product photos).
4. website at bottom of banner: www.FlexwellGoods.example (would be nice if "Silicone" was red text and "Designs" was blue text to make the words stand out)

Target Market(s)

US Consumers - mostly married women, aged 24 to 54

Industry/Entity Type

Marketing

Requirements
Must have
• Logo
• Company Name
• Tag Name (in project description)
• Website URL
Nice to have
• any other marketing sales copy or ideas. Open to appropriate stock photos.
• Other words to include (perhaps bullet points):
• "Quality Materials"
• "Designed in the USA"
• "Dishwasher Safe items"
• "Microwave Safe items"
• "Free Extended Warranty"
• "100% Satisfaction
• Guarantee"

```html
<!DOCTYPE html>
<html lang="en">
<head>
<meta charset="utf-8">
<title>Flexwell Goods – Roll-up Banner</title>
<link href="https://fonts.googleapis.com/css2?family=Open+Sans:wght@400;700;800&family=Satisfy&display=swap" rel="stylesheet">
<style>
  :root {
    --brand-red: #ee1c36;
    --brand-blue: #2a55e8;
    --brand-pink: #f26d8a;
    --stage: #dde3e3;
    --paper: #ffffff;
    --mist: #eef0f2;
    --ink: #4a4a4a;
    --steel: #c3c7cc;
    --charcoal: #2b2b2d;
  }
  * { box-sizing: border-box; margin: 0; padding: 0; }
  html, body { width: 1200px; height: 1200px; overflow: hidden; }
  body { background: var(--stage); font-family: "Open Sans", Arial, sans-serif; }

  .banner-frame {
    position: absolute; left: 372px; top: 62px;
    width: 456px; height: 1074px;
    box-shadow: 0 14px 24px rgba(60, 80, 200, 0.22);
  }
  .banner {
    position: absolute; left: 0; top: 0;
    width: 570px; height: 1343px;
    transform: scale(0.8); transform-origin: 0 0;
    background: var(--paper);
    overflow: hidden;
  }
  .abs { position: absolute; }

  .hero-backdrop {
    left: 0; top: 0; width: 570px; height: 730px;
    background: linear-gradient(180deg, #eef0f1 0%, #e4e7ea 55%, #eceef0 100%);
  }
  .hero-photo {
    left: 150px; top: 36px; width: 420px; height: 694px;
    border-radius: 190px 190px 0 0;
    background:
      linear-gradient(180deg, #ffffff 0%, #f7f8fa 22%, #e9ecf2 60%, #dfe3ea 100%);
  }

  .brand-mark {
    left: 60px; top: 92px;
    display: flex; align-items: center; gap: 10px; white-space: nowrap;
  }
  .brand-mark .dot {
    width: 30px; height: 30px; border-radius: 50%; background: var(--brand-blue); flex: none;
  }
  .brand-mark .name { font-weight: 800; font-size: 27px; color: var(--brand-red); }

  .tagline-panel { left: 0; top: 193px; width: 352px; height: 147px; }
  .tagline {
    left: 0; top: 193px; width: 285px; height: 147px;
    display: flex; flex-direction: column; align-items: center; justify-content: center;
    color: #fff; text-align: center;
  }
  .tagline .strong { font-weight: 800; font-size: 18.5px; letter-spacing: 0.2px; line-height: 1.2; }
  .tagline .script { font-family: "Satisfy", "Brush Script MT", cursive; font-size: 24px; line-height: 1.3; margin: 5px 0 3px; }

  .product-bubble {
    width: 114px; height: 114px; border-radius: 50%;
    border: 3px dashed var(--brand-blue);
    background-color: #fff;
  }
  .bubble-muffin { background: linear-gradient(160deg, #fff 0%, #fff 18%, #f04456 19%, #d8182e 60%, #fff 61%, #f04456 70%, #d8182e 100%); }
  .bubble-loaf { background: linear-gradient(200deg, #e32a3c 0%, #c61a2c 42%, #fff 43%, #fff 55%, #e32a3c 56%, #b8172a 100%); }
  .bubble-tools { background: linear-gradient(135deg, #fff 0%, #2e2e31 25%, #2e2e31 45%, #fff 46%, #fff 55%, #e12436 56%, #e12436 75%, #fff 76%); }
  .bubble-lids { background: linear-gradient(180deg, #e8e0cf 0%, #e8e0cf 14%, #e52236 15%, #e52236 32%, #fff 33%, #fff 45%, #ee3344 46%, #d3182c 100%); }
  .bubble-pops { background: linear-gradient(120deg, #f6d33c 0%, #f29a2e 20%, #ea3b4e 40%, #9d4fd0 58%, #3f7ee8 76%, #4bc36a 100%); }

  .features {
    left: 85px; top: 750px; width: 480px;
    display: grid; grid-template-columns: 240px 240px; row-gap: 12px;
    color: #fff; font-size: 14.5px; line-height: 18px;
  }
  .features li { list-style: none; position: relative; padding-left: 13px; white-space: nowrap; }
  .features li::before {
    content: ""; position: absolute; left: 0; top: 8px;
    width: 3px; height: 3px; border-radius: 50%; background: #fff;
  }

  .product-shot { border-radius: 14px; }
  .shot-stand { border-radius: 40px 40px 30px 30px; background: linear-gradient(180deg, #e32436 0%, #b81b2c 30%, #2c2c2f 45%, #1c1c1e 100%); }
  .shot-bowls { border-radius: 50% 50% 45% 45% / 20% 20% 60% 60%; background: linear-gradient(180deg, #e7e9ec 0%, #c6cad0 55%, #9aa0a7 80%, #1f1f21 81%, #1f1f21 100%); }
  .shot-lid { border-radius: 50%; background: linear-gradient(180deg, #ef3344 0%, #c9172a 100%); }
  .shot-pitcher { border-radius: 12px; background: linear-gradient(180deg, #f3d9a4 0%, #e9a43c 55%, #d9472a 100%); }
  .shot-opener { border-radius: 12px; background: linear-gradient(160deg, #f1c9b4 0%, #e23144 50%, #2d3a25 100%); }
  .shot-pan { border-radius: 50% / 40%; background: linear-gradient(180deg, #d85a36 0%, #6b9a3c 30%, #2a2a2c 55%, #2a2a2c 80%, #e22a3a 81%, #e22a3a 100%); }
  .shot-spoons { border-radius: 18px; background: linear-gradient(150deg, #55575c 0%, #3a3b3f 55%, #e02437 56%, #c21a2c 100%); }
  .shot-knives { border-radius: 10px; background: linear-gradient(180deg, #d7dadf 0%, #b9bdc3 50%, #1f1f22 51%, #1f1f22 100%); }
  .shot-shears { border-radius: 40% 20% 40% 20%; background: linear-gradient(135deg, #c9ccd1 0%, #9aa0a7 40%, #e22a3a 41%, #b8172a 100%); }

  .footer-arc { left: -40px; top: 1240px; width: 650px; height: 140px; border-radius: 50% 50% 0 0 / 30px 30px 0 0; background: var(--mist); }
  .website {
    left: 0; top: 1279px; width: 570px; text-align: center;
    font-size: 16px; line-height: 22px; color: var(--ink);
  }
  .website .red { color: var(--brand-red); font-weight: 700; }
  .website .blue { color: var(--brand-blue); }
</style>
</head>
<body>
<div class="banner-frame">
  <div class="banner">

    <div class="abs hero-backdrop"></div>
    <div class="abs hero-photo" role="img" aria-label="Smiling chef in white jacket and hat with arms crossed in a bright kitchen"></div>

    <svg class="abs" style="left:0;top:0" width="570" height="40" viewBox="0 0 570 40">
      <rect width="570" height="18" fill="var(--brand-blue)"/>
      <path d="M300 18 H570 V36 C470 28 380 22 300 18 Z" fill="var(--brand-red)"/>
      <path d="M0 18 H110 C70 22 35 28 0 34 Z" fill="var(--brand-pink)"/>
      <path d="M0 20 C150 15 420 15 570 20" fill="none" stroke="#fff" stroke-width="1.2" stroke-dasharray="4 3"/>
    </svg>

    <div class="abs brand-mark">
      <span class="dot"></span>
      <span class="name">Flexwell Goods</span>
    </div>

    <svg class="abs tagline-panel" width="352" height="147" viewBox="0 0 352 147">
      <polygon points="0,0 352,0 352,96 300,147 0,147" fill="var(--brand-red)"/>
    </svg>
    <div class="abs tagline">
      <span class="strong">QUALITY PRODUCTS</span>
      <span class="script">to Make</span>
      <span class="strong">EVERYDAY LIFE EASIER</span>
    </div>

    <div class="abs product-bubble bubble-muffin" style="left:73px;top:344px" role="img" aria-label="Red silicone muffin pans"></div>
    <div class="abs product-bubble bubble-loaf" style="left:28px;top:478px" role="img" aria-label="Red silicone loaf pans"></div>
    <div class="abs product-bubble bubble-tools" style="left:135px;top:594px" role="img" aria-label="Kitchen utensil set on stand with tongs"></div>
    <div class="abs product-bubble bubble-lids" style="left:296px;top:611px" role="img" aria-label="Set of red silicone lids"></div>
    <div class="abs product-bubble bubble-pops" style="left:444px;top:596px" role="img" aria-label="Colourful silicone ice pop molds"></div>

    <svg class="abs" style="left:0;top:700px" width="570" height="175" viewBox="0 0 570 175">
      <path d="M0 16 C150 6 300 20 570 42 V50 H0 Z" fill="var(--brand-red)"/>
      <path d="M420 22 C480 26 530 30 570 36 V14 Z" fill="var(--brand-pink)"/>
      <path d="M0 48 C200 30 380 30 570 40 V150 H0 Z" fill="var(--brand-blue)"/>
      <path d="M0 135 H570 V150 C420 160 260 165 0 165 Z" fill="var(--brand-blue)"/>
      <path d="M0 150 C150 145 300 150 570 150 V170 C480 160 300 158 150 160 Z" fill="var(--brand-red)"/>
      <path d="M0 150 C30 152 70 158 110 165 L0 168 Z" fill="var(--brand-pink)"/>
      <path d="M0 46 C200 32 380 30 570 40" fill="none" stroke="#fff" stroke-width="1.2" stroke-dasharray="4 3"/>
      <path d="M0 146 C200 152 380 150 570 144" fill="none" stroke="#fff" stroke-width="1.2" stroke-dasharray="4 3"/>
    </svg>

    <ul class="abs features">
      <li>100% Satisfaction Guarantee</li>
      <li>Microwave Safe items</li>
      <li>Quality Materials</li>
      <li>Dishwasher Safe items</li>
      <li>Free Extended Warranty</li>
      <li>Designed in the USA</li>
    </ul>

    <div class="abs product-shot shot-stand" style="left:68px;top:876px;width:70px;height:174px" role="img" aria-label="Black and red utensil set on rotating stand"></div>
    <div class="abs product-shot shot-bowls" style="left:208px;top:898px;width:158px;height:138px" role="img" aria-label="Nested stainless steel mixing bowls"></div>
    <div class="abs product-shot shot-lid" style="left:388px;top:902px;width:74px;height:40px" role="img" aria-label="Silicone lid with tongs"></div>
    <div class="abs product-shot shot-lid" style="left:476px;top:902px;width:80px;height:40px" role="img" aria-label="Silicone lid stretched over a bowl"></div>
    <div class="abs product-shot shot-pitcher" style="left:394px;top:956px;width:60px;height:78px" role="img" aria-label="Iced drink pitcher on silicone trivet"></div>
    <div class="abs product-shot shot-opener" style="left:478px;top:952px;width:74px;height:80px" role="img" aria-label="Hand using red silicone jar opener"></div>
    <div class="abs product-shot shot-pan" style="left:392px;top:1040px;width:165px;height:70px" role="img" aria-label="Frying pan of vegetables on red silicone trivet"></div>
    <div class="abs product-shot shot-spoons" style="left:25px;top:1102px;width:160px;height:112px" role="img" aria-label="Red handled slotted spoons and spatulas"></div>
    <div class="abs product-shot shot-knives" style="left:212px;top:1104px;width:148px;height:96px" role="img" aria-label="Knife set on magnetic strip"></div>
    <div class="abs product-shot shot-shears" style="left:412px;top:1140px;width:112px;height:90px" role="img" aria-label="Red handled kitchen shears"></div>

    <div class="abs footer-arc"></div>
    <div class="abs website">www.<span class="red">Flexwell</span><span class="blue">Goods</span>.example</div>

    <svg class="abs" style="left:0;top:1300px" width="570" height="43" viewBox="0 0 570 43">
      <path d="M0 6 C140 10 260 18 330 24 L0 24 Z" fill="var(--brand-red)"/>
      <path d="M460 24 C500 18 540 10 570 6 V24 Z" fill="var(--brand-pink)"/>
      <rect y="24" width="570" height="19" fill="var(--brand-blue)"/>
      <path d="M0 24 H570" fill="none" stroke="#fff" stroke-width="1.2" stroke-dasharray="4 3"/>
    </svg>

  </div>
</div>
</body>
</html>
```